Web form face-lift for an online startup

We are a web startup building a SaaS application for the freight industry. The project is mainly dedicated to the paint the main form that our customer are using along the search results that the they get. All details are in the attached documents.
Updates
The application serves the Freight Forwarders community so please think towards this industry when using background images, banners, colors, icons, etc. Computer and technology images are irrelevant.
Customer fields at the top of the page is actually part of the form.
Target Market(s)
Usually business users (Sales people, procurement, shippers, freight forwarders). Some are less tech savvy and some appreciate the new trendy web apps.
Industry/Entity Type
Building
Colors
Designer to choose colors to be used in the design.
Look and feel
Each slider illustrates characteristics of the customer's brand and the style your logo design should communicate.

```html
<!DOCTYPE html>
<html lang="en">
<head>
<meta charset="utf-8">
<title>Search for Quotes</title>
<link rel="stylesheet" href="https://fonts.googleapis.com/css2?family=Tinos:wght@400;700&display=swap">
<style>
:root{
  --ink:#111111;
  --band:#0a0af2;
  --band-dark:#0505b8;
  --teal:#bde8ea;
  --teal-light:#e3f7f8;
  --teal-dark:#8fcfd3;
  --tab-active:#2b2bc8;
  --tab-bg:#eef8fa;
  --pallet:#b9a98a;
  --pallet-light:#e2d6ba;
  --container:#2f5a9e;
  --container-light:#5f8fd0;
  --mail:#8ec6ee;
  --check:#1a2fd0;
  --link:#1a45e6;
  --stop:#d42020;
  --page:#ffffff;
  --shadow:rgba(0,0,0,.28);
}
*{box-sizing:border-box;margin:0;padding:0}
html,body{width:1200px;height:809px;overflow:hidden;background:var(--page)}
body{position:relative;font-family:"Tinos",serif;color:var(--ink);line-height:1.15}
.abs{position:absolute}
a{color:inherit;text-decoration:none}

/* header */
.logo{left:135px;top:18px;width:198px;height:43px;border:2px solid var(--ink);display:flex;align-items:center;justify-content:center;overflow:hidden}
.logo svg{position:absolute;left:0;top:0}
.logo-text{position:relative;font-size:15px;background:var(--page);padding:0 3px;line-height:16px}
.util{top:8px;font-size:14px;display:flex;align-items:center;gap:3px}
.caret{display:inline-block;width:0;height:0;border-left:10px solid transparent;border-right:10px solid transparent;border-top:10px solid var(--ink)}
.username{left:1017px;top:8px;font-size:14px;text-decoration:underline}
.globe{left:639px;top:54px}
.menu{left:675px;top:57px;font-size:14px;display:flex;gap:7px}
.band{background:linear-gradient(var(--band),var(--band) 70%,var(--band-dark));box-shadow:0 2px 3px var(--shadow)}

/* form */
h1.title{left:134px;top:98px;font-size:26px;font-weight:400;letter-spacing:-.3px}
.label-lg{font-size:19px}
.field{border:2px solid var(--ink);background:#fff;box-shadow:inset 1px 2px 3px rgba(0,0,0,.15);border-radius:2px}
.checkbox{width:11px;height:11px;border:2px solid var(--ink);background:#fff}
.tab{border:2px solid var(--ink);background:var(--tab-bg);padding:4px;box-shadow:1px 1px 3px var(--shadow)}
.tab.active{background:var(--tab-active);box-shadow:none}
.tab .art{width:100%;height:100%;border-radius:5px;box-shadow:0 0 0 3px rgba(255,255,255,.85)}
.rule{left:124px;width:977px;height:3px;background:var(--ink)}
.col-head{top:271px;font-size:19px}
.select{border:3px solid var(--ink);border-radius:9px;background:linear-gradient(var(--teal-light),var(--teal) 55%,var(--teal-dark));display:flex;align-items:center;justify-content:space-between;padding:0 8px;box-shadow:1px 2px 3px var(--shadow)}
.select .caret{border-left-width:11px;border-right-width:11px;border-top-width:11px}
.pill{border:2px solid var(--ink);border-radius:10px;background:linear-gradient(var(--teal-light),var(--teal) 60%,var(--teal-dark));font-size:12px;display:flex;align-items:center;justify-content:center;gap:4px;box-shadow:1px 1px 2px var(--shadow)}
.pill .box{width:9px;height:9px;border:1.5px solid var(--ink);background:#fff}
.pill.light{background:#fff}
.tick{color:var(--check);font-weight:700}
.hazard{border:3px solid var(--ink);border-radius:8px;background:linear-gradient(var(--teal-light),var(--teal) 60%,var(--teal-dark));display:flex;align-items:center;gap:3px;padding-left:10px;box-shadow:1px 2px 3px var(--shadow)}
.btn{border:3px solid var(--ink);border-radius:8px;background:linear-gradient(var(--teal-light),var(--teal) 55%,var(--teal-dark));font-size:25px;display:flex;align-items:center;justify-content:center;gap:2px;letter-spacing:-.3px;box-shadow:2px 3px 4px var(--shadow)}

/* footer */
.footer-links{left:56px;top:779px;font-size:24px;display:flex;gap:18px;letter-spacing:-.4px}
.social{left:788px;top:779px;display:flex;align-items:center;gap:9px;font-size:15px;font-weight:700}
.social .blog{font-size:24px;font-weight:400;letter-spacing:-.4px}
.social .sq{display:inline-block;width:10px;height:10px;background:var(--ink);margin-right:3px}
</style>
</head>
<body>
<header>
  <div class="abs logo">
    <svg width="194" height="39" viewBox="0 0 194 39"><path d="M0 0L194 39M0 39L194 0" stroke="#111" stroke-width="1.5"/></svg>
    <span class="logo-text">LOGO</span>
  </div>
  <div class="abs util" style="left:884px">USD <i class="caret"></i></div>
  <div class="abs util" style="left:943px">English <i class="caret"></i></div>
  <a class="abs username">Username</a>
  <svg class="abs globe" width="23" height="23" viewBox="0 0 23 23" role="img" aria-label="Language">
    <circle cx="11.5" cy="11.5" r="10" fill="#2a2a3a" stroke="#777" stroke-width="2"/>
    <ellipse cx="11.5" cy="11.5" rx="4.5" ry="10" fill="none" stroke="#c44" stroke-width="1"/>
    <path d="M2 11.5H21" stroke="#c44" stroke-width="1"/>
  </svg>
  <nav class="abs menu"><a>Menu item 1</a><a>Menu item 2</a><a>Menu item 3</a><a>Menu item 4</a><a>Menu item 5</a></nav>
  <div class="abs band" style="left:43px;top:77px;width:1123px;height:13px"></div>
</header>

<main>
  <h1 class="abs title">Search for Quotes</h1>
  <label class="abs label-lg" style="left:137px;top:144px">Customer</label>
  <div class="abs field" style="left:230px;top:142px;width:277px;height:30px"></div>

  <div class="abs checkbox" style="left:135px;top:207px"></div>
  <div class="abs" style="left:153px;top:204px;font-size:13px">Rate quote<sup>?</sup></div>

  <div class="abs tab active" style="left:390px;top:190px;width:94px;height:77px"><div class="art" role="img" aria-label="Boxes on a pallet" style="background:linear-gradient(135deg,var(--pallet-light),var(--pallet) 60%,#8a7a5c)"></div></div>
  <div class="abs tab" style="left:487px;top:205px;width:92px;height:62px"><div class="art" role="img" aria-label="Shipping container" style="background:linear-gradient(135deg,var(--container-light),var(--container) 60%,#1d3d70)"></div></div>
  <div class="abs tab" style="left:583px;top:205px;width:91px;height:62px">
    <svg width="83" height="54" viewBox="0 0 83 54" role="img" aria-label="Message">
      <defs><linearGradient id="mailFill" x1="0" y1="0" x2="0" y2="1"><stop offset="0" stop-color="#c4e3f8"/><stop offset="1" stop-color="var(--mail)"/></linearGradient></defs>
      <rect x="6" y="6" width="71" height="42" rx="3" fill="url(#mailFill)" stroke="#3a7cc0" stroke-width="2"/>
      <path d="M6 6L41 32L77 6" fill="none" stroke="#fff" stroke-width="3"/>
    </svg>
  </div>

  <div class="abs rule" style="top:264px"></div>
  <div class="abs col-head" style="left:149px">Qty</div>
  <div class="abs col-head" style="left:202px">Stacklabel</div>
  <div class="abs col-head" style="left:298px">Load</div>
  <div class="abs col-head" style="left:564px">Length</div>
  <div class="abs col-head" style="left:663px">Width</div>
  <div class="abs col-head" style="left:759px">Height</div>
  <div class="abs col-head" style="left:940px">Weight</div>

  <div class="abs field" style="left:135px;top:300px;width:51px;height:33px"></div>
  <svg class="abs" style="left:224px;top:304px" width="22" height="20" viewBox="0 0 22 20" role="img" aria-label="Checked"><rect x="3" y="7" width="10" height="10" fill="#fff" stroke="#111" stroke-width="2"/><path d="M4 11L8 15L20 2" fill="none" stroke="var(--check)" stroke-width="3"/></svg>
  <div class="abs select" style="left:289px;top:299px;width:252px;height:35px;font-size:19px">Box / Pallet <i class="caret"></i></div>
  <div class="abs field" style="left:547px;top:300px;width:83px;height:33px"></div>
  <div class="abs field" style="left:641px;top:300px;width:84px;height:33px"></div>
  <div class="abs field" style="left:737px;top:300px;width:83px;height:33px"></div>
  <div class="abs select" style="left:830px;top:298px;width:76px;height:35px;font-size:18px">Cm <i class="caret"></i></div>
  <div class="abs field" style="left:908px;top:300px;width:112px;height:33px"></div>
  <div class="abs select" style="left:1023px;top:299px;width:77px;height:35px;font-size:18px">Kg <i class="caret"></i></div>

  <div class="abs pill" style="left:133px;top:344px;width:130px;height:23px;font-size:11px">+ Add more units</div>

  <div class="abs rule" style="top:372px"></div>
  <div class="abs" style="left:685px;top:388px;font-size:12px">Total</div>
  <div class="abs field" style="left:719px;top:381px;width:78px;height:33px"></div>
  <div class="abs field" style="left:805px;top:381px;width:73px;height:33px"></div>
  <div class="abs select" style="left:882px;top:380px;width:69px;height:35px;font-size:14px;padding:0 4px">CMB <i class="caret"></i></div>
  <div class="abs field" style="left:956px;top:381px;width:66px;height:33px"></div>
  <div class="abs select" style="left:1023px;top:380px;width:77px;height:35px;font-size:18px">Kg <i class="caret"></i></div>
  <div class="abs rule" style="top:427px"></div>

  <div class="abs" style="left:138px;top:468px;font-size:14px">From :</div>
  <div class="abs field" style="left:193px;top:463px;width:357px;height:31px;font-size:14px;text-align:center;line-height:27px">Shipping address or port</div>
  <svg class="abs" style="left:555px;top:464px" width="125" height="30" viewBox="0 0 125 30">
    <defs><linearGradient id="arrowFill" x1="0" y1="0" x2="0" y2="1"><stop offset="0" stop-color="#b8d6f6"/><stop offset="1" stop-color="#5f97d8"/></linearGradient>
    <linearGradient id="boxFill" x1="0" y1="0" x2="1" y2="1"><stop offset="0" stop-color="var(--container-light)"/><stop offset="1" stop-color="#1d3d70"/></linearGradient></defs>
    <path d="M2 10H26V4L38 15L26 26V20H2Z" fill="url(#arrowFill)" stroke="#224" stroke-width="1.5"/>
    <rect x="40" y="3" width="38" height="24" fill="url(#boxFill)" role="img" aria-label="Shipping container"/>
    <path d="M85 10H109V4L121 15L109 26V20H85Z" fill="url(#arrowFill)" stroke="#224" stroke-width="1.5"/>
  </svg>
  <div class="abs" style="left:680px;top:468px;font-size:14px">To :</div>
  <div class="abs field" style="left:716px;top:463px;width:357px;height:31px;font-size:14px;text-align:center;line-height:27px">Shipping address or port</div>

  <div class="abs btn" style="left:132px;top:539px;width:131px;height:37px">
    <svg width="24" height="24" viewBox="0 0 24 24"><circle cx="12" cy="12" r="8" fill="none" stroke="#8a8aa8" stroke-width="4" stroke-dasharray="3 2.3"/><circle cx="12" cy="12" r="4" fill="#b8b8d0"/></svg>Options
  </div>
  <div class="abs pill" style="left:131px;top:580px;width:71px;height:20px;font-size:13px"><i class="box"></i>Import</div>
  <div class="abs pill" style="left:224px;top:580px;width:73px;height:20px;font-size:13px"><span class="tick">✔</span>Export</div>
  <div class="abs pill light" style="left:331px;top:579px;width:105px;height:22px;font-size:13px">Incoterm: <span style="color:var(--link)">FCA</span></div>

  <div class="abs hazard" style="left:528px;top:570px;width:79px;height:41px"><span class="tick">✔</span>
    <svg width="40" height="36" viewBox="0 0 40 36" role="img" aria-label="No fragile goods"><circle cx="20" cy="18" r="15" fill="#444"/><circle cx="20" cy="18" r="15" fill="none" stroke="var(--stop)" stroke-width="4"/><path d="M9 7L31 29" stroke="var(--stop)" stroke-width="4"/></svg>
  </div>
  <div class="abs hazard" style="left:610px;top:570px;width:79px;height:41px"><span class="tick">✔</span>
    <svg width="40" height="36" viewBox="0 0 40 36" role="img" aria-label="No perishable goods"><circle cx="20" cy="18" r="15" fill="#3a6ac0"/><circle cx="20" cy="18" r="15" fill="none" stroke="var(--stop)" stroke-width="4"/><path d="M9 7L31 29" stroke="var(--stop)" stroke-width="4"/></svg>
  </div>
  <div class="abs hazard" style="left:693px;top:570px;width:79px;height:41px"><span class="tick">✔</span>
    <svg width="40" height="36" viewBox="0 0 40 36" role="img" aria-label="Radioactive goods"><circle cx="20" cy="18" r="16" fill="#f2c400"/><circle cx="20" cy="18" r="3" fill="#222"/><path d="M20 18L12 5A15 15 0 0 1 28 5Z M20 18L35 18A15 15 0 0 1 27 31Z M20 18L13 31A15 15 0 0 1 5 18Z" fill="#222"/></svg>
  </div>

  <div class="abs select" style="left:843px;top:572px;width:255px;height:36px;font-size:25px;padding:0 12px">Price level <i class="caret"></i></div>
  <div class="abs pill" style="left:1006px;top:625px;width:91px;height:23px;font-size:11px">⚙ More options</div>

  <div class="abs btn" style="left:271px;top:682px;width:317px;height:39px">
    <svg width="48" height="30" viewBox="0 0 48 30"><line x1="2" y1="27" x2="30" y2="17" stroke="#222" stroke-width="3"/><circle cx="36" cy="12" r="8" fill="#e8ecf4" stroke="#555" stroke-width="2"/></svg>Search Quote
  </div>
  <div class="abs btn" style="left:650px;top:682px;width:317px;height:39px">
    <svg width="30" height="28" viewBox="0 0 30 28" role="img" aria-label="Manual entry"><path d="M6 26C3 22 3 16 5 12L8 6C9 4 11 5 11 7V12L13 3C14 1 16 2 16 4V11L18 2C19 0 21 1 21 3V12L23 6C24 4 26 5 26 7L24 18C23 23 20 26 15 26Z" fill="#d8d8d8" stroke="#777" stroke-width="1.3"/></svg>Create manually
  </div>
</main>

<footer>
  <div class="abs band" style="left:45px;top:760px;width:1121px;height:11px"></div>
  <nav class="abs footer-links"><a>About us</a><a>Privacy policy</a><a>Terms of service</a><a>News</a></nav>
  <div class="abs social">
    <a class="blog">Blog</a>
    <a><i class="sq"></i>Gatherly</a>
    <a>Chirpa</a>
    <a>Proflink</a>
    <a>Vidstream</a>
  </div>
</footer>
</body>
</html>
```